Upsell Vertical Banner Ad Design For B2B Marketing Agency Vertical 768px × 1180px IS THE SIZE

I need a banner made for my website www.brightlanepromotionhub.biz This banner will be an upsell advertisement for after someone signs up for my monthly program. When they login to their account for the 1st time I will give them the chance to upgrade their account to our annual program with just one click.

this is a page that upsells it currently to give you an idea how we market ourselves:
https://tlpx.pagevault-example.com/page/tlp-annual-upsell

Use this content:

Are You Ready To Commit To Taking Your Business To The Next Level?

Because We're In This For The Long-Haul and Dedicated To Your Success...

Save $300 By Upgrading To An Annual Membership And Pay Only $74/mth

((BUTTON))Yes, Upgrade My Plan Right Now!

*Must prepay the full year at only $898/yr!

Target Market(s)

business owners

Industry/Entity Type

Marketing

Requirements
Must have
• 768px × 1180px IS THE SIZE vertical

Use this content:

Nice to have
• Use this content:

Should not have
• Use this content:

```html
<!DOCTYPE html>
<html lang="en">
<head>
<meta charset="utf-8">
<title>Annual Membership Upgrade</title>
<link rel="stylesheet" href="https://fonts.googleapis.com/css2?family=Archivo+Black&family=Source+Sans+3:wght@600;700;800&display=swap">
<style>
  :root {
    --green-light: #93c01f;
    --green-mid: #5f9a2c;
    --green-deep: #2f5f24;
    --rule-green: #006838;
    --panel-light: #fafafa;
    --panel-edge: #dcdcdc;
    --grey-soft: #808080;
    --grey-strong: #636363;
    --ink: #000000;
    --white: #ffffff;
  }
  * { margin: 0; padding: 0; box-sizing: border-box; }
  html, body { width: 781px; height: 1200px; overflow: hidden; background: var(--white); }
  .banner { position: relative; width: 781px; height: 1200px; font-family: "Source Sans 3", "Myriad Pro", sans-serif; }

  .panel {
    position: absolute; left: 3px; top: 300px; width: 775px; height: 897px;
    border-radius: 0 0 56px 56px;
    background: radial-gradient(ellipse 70% 60% at 50% 35%, var(--panel-light) 55%, var(--panel-edge) 100%);
  }
  .header {
    position: absolute; left: 0; top: 0; width: 781px; height: 398px;
    border-radius: 50px 50px 0 0;
    background:
      radial-gradient(ellipse 65% 55% at 50% 22%, rgba(147,192,31,1) 30%, rgba(147,192,31,0) 100%),
      linear-gradient(to bottom, var(--green-mid) 0%, var(--green-mid) 70%, var(--green-deep) 100%);
  }
  .pointer { position: absolute; left: 348px; top: 397px; width: 84px; height: 45px; }

  .headline {
    position: absolute; left: 47px; top: 64px;
    font-family: "Archivo Black", "Arial Black", sans-serif;
    font-size: 59px; line-height: 76px; letter-spacing: 2.4px;
    color: var(--white); text-transform: uppercase; white-space: nowrap;
  }

  .subhead {
    position: absolute; left: 0; width: 781px; top: 460px;
    text-align: center; color: var(--grey-soft);
    font-weight: 600; font-size: 43px; line-height: 51px; letter-spacing: -0.3px;
  }
  .rule { position: absolute; left: 91px; top: 632px; width: 607px; height: 3px; background: var(--rule-green); }

  .offer { position: absolute; left: 0; width: 781px; text-align: center; color: var(--grey-strong); font-weight: 700; white-space: nowrap; line-height: 1; }
  .offer .big { font-size: 64px; font-weight: 800; }
  .offer .mid { font-size: 45px; }
  .offer-1 { top: 646px; }
  .offer-2 { top: 718px; }
  .offer-3 { top: 772px; }

  .cta {
    position: absolute; left: 102px; top: 861px; width: 576px; height: 185px;
    border-radius: 40px;
    background:
      radial-gradient(ellipse 60% 55% at 50% 20%, rgba(147,192,31,1) 25%, rgba(147,192,31,0) 100%),
      linear-gradient(to bottom, var(--green-mid) 0%, var(--green-mid) 60%, var(--green-deep) 100%);
    color: var(--white); text-align: center; text-decoration: none; font-weight: 700; line-height: 1;
  }
  .cta-line { position: absolute; left: 0; width: 100%; white-space: nowrap; }
  .cta-top { top: 27px; font-size: 53px; letter-spacing: -0.5px; }
  .cta-main { top: 83px; font-size: 70px; }

  .terms { position: absolute; left: 0; width: 781px; text-align: center; color: var(--ink); line-height: 1; white-space: nowrap; }
  .terms-1 { top: 1062px; font-size: 50px; font-weight: 600; letter-spacing: -0.3px; }
  .terms-2 { top: 1111px; font-size: 68px; font-weight: 800; }
</style>
</head>
<body>
<div class="banner">
  <div class="panel"></div>
  <div class="header"></div>
  <svg class="pointer" viewBox="0 0 84 45" aria-hidden="true">
    <path d="M0 0 H84 L42 44 Z" fill="#2f5f24"/>
  </svg>

  <h1 class="headline">Are You Ready To<br>Commit To Taking<br>Your Business To<br>The Next Level?</h1>

  <p class="subhead">Because We're In This For The<br>Long-Haul and Dedicated To<br>Your Success...</p>

  <div class="rule"></div>

  <p class="offer offer-1"><span class="big">Save $300</span> <span class="mid">By Upgrading To</span></p>
  <p class="offer offer-2"><span class="mid">An Annual Membership And</span></p>
  <p class="offer offer-3"><span class="mid">Pay</span> <span class="big">Only $74/mth</span></p>

  <a class="cta" href="#upgrade">
    <span class="cta-line cta-top">Yes, Upgrade My Plan</span>
    <span class="cta-line cta-main">Right Now!</span>
  </a>

  <p class="terms terms-1">*Must prepay the full year at</p>
  <p class="terms terms-2">only $898/yr!</p>
</div>
</body>
</html>
```